Progressive Architecture and Urban Planning Studio - Stationery Design

The Kestrel Collective: a small boutique Architectural and Urban Planning Studio based in Natal/ RN, Brazil, about to open branches in South Africa and West Africa, established to provide high quality, innovative design and personal client service for projects worldwide. Our approach to Architecture: Minimal - Less is More, so to speak, but with an edge! Strive to produce "clean" projects - stripped of all that can be stripped, no excesses. Got our Logo right here with Pixel Harbor, and hope to do the same with our stationery (were informed that includes business cards, letterhead and envelopes). Since we'll be using two clour schemes, we want at least one using a black background (business card). We'll also allow manipulation of our logo if it helps the final design. Good Luck!

Industry/Entity Type

Business

Other font styles liked:
• Nexa

Colors

Designer to choose colors to be used in the design.

Requirements
Must have
• Business Cards/ Letterheads with the following address:
Rua Benedito Sarmento 742, Jardim Aurora, Vale Alto/RN
Should be able to edit it.

```html
<!DOCTYPE html>
<html lang="en">
<head>
<meta charset="utf-8">
<title>The Kestrel Collective — Stationery</title>
<link rel="stylesheet" href="https://fonts.googleapis.com/css2?family=Montserrat:wght@400;500&family=Open+Sans:wght@400&display=swap">
<style>
  :root {
    --board: #717173;
    --paper: #ffffff;
    --red: #d9141b;
    --red-deep: #a8060d;
    --ink: #3a3a3a;
    --ink-soft: #5b5b5b;
    --name: #1f1f1f;
  }
  * { margin: 0; padding: 0; box-sizing: border-box; }
  html, body { width: 1200px; height: 2429px; overflow: hidden; background: var(--paper); }
  .canvas { position: relative; width: 1200px; height: 2429px; }
  .board { position: absolute; left: 27px; top: 0; width: 1148px; height: 2092px; background: var(--board); }
  .sheet { position: absolute; background: var(--paper); }

  .wordmark {
    font-family: "Montserrat", sans-serif; font-weight: 500;
    text-transform: uppercase; color: var(--name); white-space: nowrap;
    display: flex; align-items: center;
  }
  .wordmark .mark-square { display: inline-block; background: var(--red); margin-right: 0.7em; }

  .logo-card { left: 65px; top: 42px; width: 427px; height: 245px; }
  .logo-card .wordmark { position: absolute; left: 0; right: 0; top: 208px; justify-content: center; font-size: 19px; letter-spacing: 0.22em; }
  .logo-card .mark-square { width: 22px; height: 22px; }

  .business-card { left: 68px; top: 317px; width: 425px; height: 245px; }
  .business-card .card-logo { position: absolute; top: 44px; left: 0; width: 100%; justify-content: center; font-size: 13px; letter-spacing: 0.2em; }
  .business-card .card-logo .mark-square { width: 16px; height: 16px; }
  .name-band {
    position: absolute; left: 0; top: 106px; width: 100%; height: 30px;
    background: linear-gradient(90deg, var(--red), var(--red-deep));
    color: #fff; font-family: "Open Sans", sans-serif; font-size: 15px;
    display: flex; align-items: center; justify-content: center; text-transform: uppercase;
  }
  .name-band .role { text-transform: none; font-size: 13px; margin-left: 4px; }
  .card-address {
    position: absolute; left: 8px; width: 200px; top: 174px; text-align: right;
    font-family: "Open Sans", sans-serif; font-size: 12px; line-height: 1.4; color: var(--ink);
  }
  .card-divider { position: absolute; left: 214px; top: 161px; width: 2px; height: 60px; background: var(--red); }
  .card-contacts {
    position: absolute; left: 240px; top: 159px; list-style: none;
    font-family: "Open Sans", sans-serif; font-size: 12.5px; line-height: 1.9; color: var(--ink);
  }

  .letterhead { left: 68px; top: 602px; width: 992px; height: 1401px; }
  .letterhead .sheet-logo { position: absolute; top: 74px; left: 0; width: 100%; justify-content: center; font-size: 25px; letter-spacing: 0.25em; }
  .letterhead .sheet-logo .mark-square { width: 30px; height: 30px; }
  .sheet-footer {
    position: absolute; left: 0; right: 0; bottom: 25px; height: 20px;
    font-family: "Open Sans", sans-serif; font-size: 14.5px; color: var(--ink-soft);
  }
  .sheet-footer span { position: absolute; top: 0; white-space: nowrap; }
  .sheet-footer .address { left: 50px; }
  .sheet-footer .phone { left: 489px; }
  .sheet-footer .web { right: 52px; }
</style>
</head>
<body>
<div class="canvas">
  <div class="board"></div>

  <section class="sheet logo-card" aria-label="Logo">
    <div class="wordmark"><span class="mark-square"></span>The Kestrel Collective</div>
  </section>

  <section class="sheet business-card" aria-label="Business card">
    <div class="wordmark card-logo"><span class="mark-square"></span>The Kestrel Collective</div>
    <div class="name-band">Marco Teixeira,<span class="role">Director</span></div>
    <p class="card-address">Rua Benedito Sarmento 742,<br>Jardim Aurora, Vale Alto/RN</p>
    <div class="card-divider"></div>
    <ul class="card-contacts">
      <li>0421 586 304</li>
      <li>marco@kestrelcollective.com</li>
      <li>www.kestrelcollective.com</li>
    </ul>
  </section>

  <section class="sheet letterhead" aria-label="Letterhead">
    <div class="wordmark sheet-logo"><span class="mark-square"></span>The Kestrel Collective</div>
    <footer class="sheet-footer">
      <span class="address">Rua Benedito Sarmento 742, Jardim Aurora, Vale Alto/RN</span>
      <span class="phone">0421 586 304</span>
      <span class="web">www.kestrelcollective.com</span>
    </footer>
  </section>
</div>
</body>
</html>
```